Book cover for book about ex-wifes

I need a book cover for my new book called "Tidligere brude fra Solen, Stormen og Lindevang" - In english: "Former brides from Sun, Storm and Lindevang" (Hørsholm is a posh city in Denmark).

The book is by men for men about ex-wifes and about how to avoid getting them.
Is it a book from a sexologist and couples therapist to men on how to improve relations.

Men (and curious women)

• Something that indicate three types of ex-wifes

And the author name “Jonas Beltoft”
• Something that says something about relationships, couples and how to stay together (or how to avoid not breaking up)
• No hate

```html
<!DOCTYPE html>
<html lang="da">
<head>
<meta charset="utf-8">
<title>Tidligere brude fra Solen, Stormen og Lindevang – omslag</title>
<link href="https://fonts.googleapis.com/css2?family=League+Spartan:wght@500;700&family=Open+Sans:wght@400&display=swap" rel="stylesheet">
<style>
  :root {
    --page: #f4f4f4;
    --paper: #ffffff;
    --spine: #f2efe8;
    --ink: #111111;
    --cyan: #2ec4cf;
    --pink: #e46aa6;
    --violet: #9a4fc4;
    --teal: #1f9fa8;
    --edge: #8a8a8a;
  }
  * { margin: 0; padding: 0; box-sizing: border-box; }
  html, body {
    width: 899px; height: 1200px; overflow: hidden;
    background: var(--page);
  }
  .spread {
    position: absolute;
    left: 10px; top: 296px;
    width: 880px; height: 609px;
    background: var(--paper);
    box-shadow: 0 0 0 1px var(--edge), 2px 3px 6px rgba(0,0,0,.25);
    overflow: hidden;
  }
  .title {
    font-family: "League Spartan", sans-serif;
    font-weight: 700;
    line-height: 1.02;
    text-transform: uppercase;
    white-space: nowrap;
  }
  .title .line-one { color: var(--cyan); display: block; font-weight: 500; }
  .title .line-two { color: var(--ink); display: block; }
  .author {
    font-family: "League Spartan", sans-serif;
    font-weight: 700;
    text-transform: uppercase;
    color: var(--ink);
    white-space: nowrap;
  }

  /* back cover */
  .back-cover { position: absolute; left: 0; top: 0; width: 406px; height: 609px; }
  .back-cover .title { position: absolute; left: 70px; top: 84px; font-size: 19px; }
  .blurb {
    position: absolute; left: 70px; top: 150px; width: 268px;
    font-family: "Open Sans", sans-serif;
    font-size: 9.6px; line-height: 12.4px;
    color: var(--ink); text-align: justify; hyphens: auto;
  }
  .blurb p + p { margin-top: 12.4px; }

  /* spine */
  .spine { position: absolute; left: 406px; top: 0; width: 68px; height: 609px; background: var(--spine); }
  .spine .title {
    position: absolute; left: 50%; top: 176px;
    font-size: 19px; text-align: left;
    transform: translate(-50%, -50%) rotate(-90deg);
  }
  .spine .author {
    position: absolute; left: 50%; top: 458px;
    font-size: 12px; letter-spacing: 15px;
    transform: translate(-50%, -50%) rotate(-90deg);
  }

  /* front cover */
  .front-cover { position: absolute; left: 474px; top: 0; width: 406px; height: 609px; }
  .front-cover .author {
    position: absolute; left: 24px; top: 38px;
    font-size: 21px; letter-spacing: 19.5px;
  }
  .front-cover .title { position: absolute; left: 24px; top: 80px; font-size: 25px; }
  .cover-art { position: absolute; left: 0; top: 170px; width: 406px; height: 439px; }
</style>
</head>
<body>
  <main class="spread">
    <section class="back-cover">
      <h2 class="title"><span class="line-one">Tidligere brude fra Solen,</span><span class="line-two">Stormen og Lindevang</span></h2>
      <div class="blurb">
        <p>Lorem ipsum dolor sit amet, consectetur adipiscing elit. Nam viverra lorem nec nibh porttitor dapibus. Donec fringilla pretium lorem, quis ultrices leo eleifend interdum. Aliquam ante diam, blandit sed scelerisque posuere, vestibulum et elit. Sed feugiat mauris orci, nec semper libero tristique at. Etiam ut est in velit facilisis placerat eget sed est. Fusce at enim nec libero vulputate cursus. Phasellus sodales eu lectus et fermentum. Aenean erat enim, pharetra eu interdum vel, elementum sit amet ex. Etiam sit amet efficitur augue, vitae malesuada nulla. Fusce a ultrices nulla. Quisque viverra luctus leo, vitae aliquam massa vehicula facilisis. Aenean iaculis imperdiet risus a dignissim. Nulla rhoncus sem ex, non molestie nulla laoreet ac. Class aptent taciti sociosqu ad litora torquent per conubia nostra, per inceptos himenaeos. Sed sagittis magna accumsan sagittis porta. Donec pretium erat at convallis dapibus.</p>
        <p>Quisque metus magna, hendrerit non eros venenatis, hendrerit feugiat diam. Fusce aliquam odio euismod, finibus ex vitae, viverra mauris. Suspendisse auctor urna eu augue bibendum consectetur. Sed eu orci vitae dolor luctus ornare. Morbi nisl risus, euismod ac pretium id, ultricies vitae libero. Sed placerat ac eros nec auctor. Nunc dignissim magna nisi, ac dictum ipsum consectetur non. Phasellus nec blandit ipsum. Donec eget nisl lacinia, aliquet justo eget, molestie felis. Pellentesque ultrices ante nec molestie consectetur. Integer in ipsum nec ipsum sollicitudin viverra.</p>
      </div>
    </section>

    <section class="spine">
      <div class="title"><span class="line-one">Tidligere brude fra Solen,</span><span class="line-two">Stormen og Lindevang</span></div>
      <div class="author">Author Name</div>
    </section>

    <section class="front-cover">
      <div class="author">Author Name</div>
      <h1 class="title"><span class="line-one">Tidligere brude fra Solen,</span><span class="line-two">Stormen og Lindevang</span></h1>
      <svg class="cover-art" viewBox="0 0 406 439" role="img" aria-label="Watercolour silhouettes of a woman pointing at a man, with three question marks above them, in pink, violet and teal">
        <defs>
          <linearGradient id="wash" x1="0" y1="0" x2="1" y2="1">
            <stop offset="0" stop-color="#f3a6c6"/>
            <stop offset="0.4" stop-color="#d35a9e"/>
            <stop offset="0.65" stop-color="#9a4fc4"/>
            <stop offset="1" stop-color="#1f9fa8"/>
          </linearGradient>
        </defs>
        <rect x="0" y="0" width="406" height="439" fill="url(#wash)" opacity="0.85"/>
      </svg>
    </section>
  </main>
</body>
</html>
```